Logo & Visitenkarte für Weinbauer
Vielen Dank für die tolle Umsetzung und unterschiedlichen Darstellungen, wo man sich dann sehen konnte, WIE das Logo wirkt. Well done!
Zielgruppe
Ich bin Weinbauer und betreibe auch einen Buschenschank. Zielgruppe ist die Gastronomie und der (Durchschnitts-) Endverbraucher.
Aufgabenstellung
Unsere Betriebsstätte ist im Veltlinerland Weinviertel (Österreich).
Wir wollen die Werte Tradition, Regional, Vertrauen und Bodenständigkeit vermitteln.
Unsere Kunden schätzen die Herkunft.
Das Logo soll als Firmenlogo und auch für die Weinetiketten verwendet werden können.

```html
<!DOCTYPE html>
<html lang="de">
<head>
<meta charset="utf-8">
<title>Weinetikett – Weinbau Steiner</title>
<link rel="stylesheet" href="https://fonts.googleapis.com/css2?family=Barlow+Condensed:wght@500&family=Barlow:wght@600&display=swap">
<style>
  :root {
    --canvas: #d9d9d9;
    --label-red: #7b3136;
    --band-red: #5c2329;
    --stripe-red: #4a1a20;
    --frame-line: #dcbcbc;
    --gold: #d8b487;
    --copy: #e6c9b0;
  }
  html, body {
    margin: 0;
    padding: 0;
    overflow: hidden;
  }
  body {
    width: 1164px;
    height: 1200px;
    background: var(--canvas);
    position: relative;
  }
  .wine-label {
    position: absolute;
    left: 232px;
    top: 100px;
    width: 700px;
    height: 1000px;
  }
  .wine-label svg {
    position: absolute;
    inset: 0;
    width: 100%;
    height: 100%;
  }
  .brand-mark {
    position: absolute;
    left: 0;
    right: 0;
    top: 130px;
    display: flex;
    flex-direction: column;
    align-items: center;
  }
  .brand-dot {
    width: 140px;
    height: 140px;
    border-radius: 50%;
    background: var(--gold);
  }
  .brand-name {
    margin-top: 34px;
    font-family: "Barlow Condensed", sans-serif;
    font-weight: 500;
    font-size: 70px;
    letter-spacing: 1px;
    line-height: 1;
    color: var(--gold);
  }
  .wine-description {
    position: absolute;
    left: 150px;
    right: 150px;
    top: 560px;
    margin: 0;
    font-family: "Barlow", sans-serif;
    font-weight: 600;
    font-size: 17px;
    line-height: 1.45;
    text-align: center;
    color: var(--copy);
  }
</style>
</head>
<body>
  <div class="wine-label">
    <svg viewBox="0 0 700 1000" aria-hidden="true">
      <defs>
        <path id="label-outline" d="M40 150 C40 40 200 10 350 10 C500 10 660 40 660 150 L660 160 L680 160 L680 760 C680 920 560 990 350 990 C140 990 20 920 20 760 L20 160 L40 160 Z"/>
        <clipPath id="label-inner">
          <use href="#label-outline" transform="translate(350 500) scale(0.9) translate(-350 -500)"/>
        </clipPath>
      </defs>
      <use class="label-body" href="#label-outline" fill="var(--label-red)"/>
      <g clip-path="url(#label-inner)">
        <rect class="top-band" x="0" y="0" width="700" height="270" fill="var(--band-red)"/>
        <rect class="bottom-band" x="0" y="790" width="700" height="210" fill="var(--band-red)"/>
        <g class="band-stripes" fill="var(--stripe-red)">
          <rect x="150" y="0" width="40" height="270"/>
          <rect x="250" y="0" width="40" height="270"/>
          <rect x="410" y="0" width="40" height="270"/>
          <rect x="510" y="0" width="40" height="270"/>
          <rect x="150" y="790" width="40" height="210"/>
          <rect x="250" y="790" width="40" height="210"/>
          <rect x="410" y="790" width="40" height="210"/>
          <rect x="510" y="790" width="40" height="210"/>
        </g>
      </g>
      <g class="frame-lines" fill="none" stroke="var(--frame-line)">
        <use href="#label-outline" transform="translate(350 500) scale(0.965) translate(-350 -500)" stroke-width="3"/>
        <use href="#label-outline" transform="translate(350 500) scale(0.9) translate(-350 -500)" stroke-width="4"/>
      </g>
    </svg>

    <div class="brand-mark">
      <div class="brand-dot"></div>
      <div class="brand-name">WEINBAUSTEINER</div>
    </div>

    <p class="wine-description">Dieser Grüne Veltliner wächst auf kargen Lössböden im Weinviertel und wird von Hand gelesen. Im Glas zeigt er helles Gelb, feine Pfefferwürze und Noten von grünem Apfel. Am Gaumen frisch, saftig und ausgewogen mit langem Abgang. Passt zu Brettljause, Backhendl und mildem Käse. Gut gekühlt bei acht bis zehn Grad genießen.</p>
  </div>
</body>
</html>
```